Business Card Design- Mortgage Firm

Looking to design a business Card for our Outside sales people. This card is used to provide their contact information to prospective clients and realtors. Must have All Pertinent company and licensing information by law. We are looking for a very modern design that flows with our current logo color scheme. Red/White/Black

Industry/Entity Type

Mortgage Lender

Contact Information for Business Card

Must stick with current color scheme.

Colors
f04a50
ffffff
ecf7fb

Requirements
Must have
• Company Logo or similar
• Company Address (748 W Alder Avenue, Suite 312, Corona CA 92879 NMLS: 4072916)
• Agent Name (Mira Talbot)
• Title (Senior Mortgage Loan Originator)
• NMLS# 8395021
• Toll Free: 800-627-3184
• Direct : 310-555-4860
Nice to have
• Room for Agent Picture

```html
<!DOCTYPE html>
<html lang="en">
<head>
<meta charset="utf-8">
<title>Halvern Mortgage – Business Card</title>
<link rel="stylesheet" href="https://fonts.googleapis.com/css2?family=Source+Sans+3:wght@400;600;700&display=swap">
<style>
  :root {
    --brand-red: #b71f26;
    --ink: #3a3a3a;
    --card-white: #ffffff;
    --page-bg: #e9ecee;
    --swoosh-dark: #2e2e30;
    --swoosh-light: #a9abaf;
    --portrait-top: #cbb9a6;
    --portrait-bottom: #3b3f4a;
  }
  * { box-sizing: border-box; margin: 0; padding: 0; }
  html, body {
    width: 1200px; height: 801px; overflow: hidden;
    background: var(--page-bg);
    font-family: "Source Sans 3", "Myriad Pro", Arial, sans-serif;
  }
  .card {
    position: absolute; left: 156px; top: 145px;
    width: 888px; height: 510px;
    background: var(--card-white);
    overflow: hidden;
    box-shadow: 0 6px 18px rgba(0,0,0,.18);
  }
  .portrait {
    position: absolute; left: 22px; top: 20px;
    width: 362px; height: 450px;
    background: linear-gradient(180deg, var(--portrait-top) 0%, #9c8570 45%, var(--portrait-bottom) 100%);
    border-radius: 160px 160px 0 0;
  }
  .wave { position: absolute; left: 0; top: 0; width: 888px; height: 510px; }
  .brand {
    position: absolute; left: 412px; top: 50px;
    display: flex; align-items: center; gap: 18px;
    color: var(--brand-red); font-weight: 600;
  }
  .brand-mark { width: 70px; height: 70px; background: var(--brand-red); }
  .brand-name { line-height: 1; }
  .brand-name .primary { display: block; font-size: 56px; letter-spacing: 2px; }
  .brand-name .secondary { display: block; font-size: 24px; letter-spacing: 11px; margin-top: 6px; }
  .contact {
    position: absolute; left: 423px; top: 190px;
    color: var(--ink); font-size: 22px; line-height: 32px;
  }
  .contact .label { color: var(--brand-red); font-weight: 700; }
  .contact .address { margin-bottom: 26px; }
  .contact .license { margin-top: 14px; }
  .agent {
    position: absolute; right: 32px; top: 396px;
    text-align: right; color: var(--card-white);
  }
  .agent-name { font-size: 36px; font-weight: 700; letter-spacing: .5px; line-height: 1; }
  .agent-title { font-size: 17px; font-weight: 400; margin-top: 16px; letter-spacing: .3px; }
</style>
</head>
<body>
  <article class="card">
    <div class="portrait" role="img" aria-label="Portrait photo of the loan originator"></div>

    <svg class="wave" viewBox="0 0 888 510" aria-hidden="true">
      <path d="M0 300 C40 350 100 400 170 432 C120 414 60 372 0 330 Z" fill="var(--swoosh-dark)"/>
      <path d="M0 322 C60 372 120 414 190 442 C130 426 70 390 0 350 Z" fill="var(--swoosh-light)"/>
      <path d="M0 345 C110 410 250 460 384 458 C500 456 560 360 888 335 L888 510 L0 510 Z" fill="var(--brand-red)"/>
      <path d="M640 366 C730 335 800 318 888 316 L888 330 C800 330 730 345 640 366 Z" fill="var(--swoosh-dark)"/>
      <path d="M660 362 C740 340 810 332 888 330 L888 336 C810 337 740 348 660 362 Z" fill="var(--swoosh-light)"/>
    </svg>

    <header class="brand">
      <span class="brand-mark"></span>
      <span class="brand-name">
        <span class="primary">HALVERN</span>
        <span class="secondary">MORTGAGE</span>
      </span>
    </header>

    <section class="contact">
      <p class="address">748 W Alder Avenue, Suite 312<br>Corona CA 92879, NMLS: 4072916</p>
      <p><span class="label">Toll Free:</span> 800-627-3184</p>
      <p><span class="label">Direct :</span> 310-555-4860</p>
      <p class="license">NMLS# 8395021</p>
    </section>

    <footer class="agent">
      <h1 class="agent-name">MIRA TALBOT</h1>
      <p class="agent-title">SENIOR MORTGAGE LOAN ORIGINATOR</p>
    </footer>
  </article>
</body>
</html>
```